Website Pravelo Onderzoek

We are a small European high-tech online research company.
With our own state of the art software we run online panels and are conducting reseach for companies. Partly research via our own panel and partly via panels we maintain for our customers.
Our current website is old and outdatet: www.pravelo.nl.
We are in the process to change the content of the site. We want a modern, european and businesslike design for our new website.
Our logo has to stay the same (left uppersite of our website and attached) but can be changed a little to adapt it to the new design of the website. The colors of the site are up to you.
Target Market(s)
Marketeers and researchers of large and middle size companies in all kind of fields.
Industry/Entity Type
Online
Look and feel
Each slider illustrates characteristics of the customer's brand and the style your logo design should communicate.

```html
<!DOCTYPE html>
<html lang="nl">
<head>
<meta charset="utf-8">
<title>Pravelo Onderzoek</title>
<link href="https://fonts.googleapis.com/css2?family=Noto+Sans:wght@400;700&family=Cousine&display=swap" rel="stylesheet">
<style>
:root{
  --red:#c4161c;
  --red-dark:#8e0f12;
  --text:#4a4a4a;
  --nav-top:#4a4a4a;
  --nav-bot:#111;
  --orange:#f26a0f;
  --rule:#bdbdbd;
  --link:#e01010;
  --page:#fff;
}
*{margin:0;padding:0;box-sizing:border-box}
html,body{width:1200px;height:1054px;overflow:hidden;background:var(--page)}
body{position:relative;font-family:"Noto Sans",sans-serif;color:var(--text);font-size:11.5px;line-height:13.6px;letter-spacing:.3px}
.backdrop{position:absolute;left:0;top:0;width:1200px;height:440px;background:linear-gradient(#e9e9e9,#f5f5f5 70%,#fff)}
.abs{position:absolute}
.logo{left:139px;top:28px;width:150px;height:150px;border-radius:50%;border:3px solid #8a8a8a;background:#f4f4f4;display:flex;align-items:center;justify-content:center;font-size:22px;font-weight:700;color:#555;letter-spacing:0}
.divider{left:302px;top:38px;width:1px;height:110px;background:#c9c9c9}
.site-title{left:323px;top:52px;font-size:34px;line-height:40px;font-weight:700;color:var(--red);letter-spacing:0}
.tagline{left:330px;top:96px;font-family:"Cousine",monospace;font-size:13px;color:#333;letter-spacing:0}
.nav{left:141px;top:167px;width:921px;height:37px;border-radius:3px;background:linear-gradient(var(--nav-top),var(--nav-bot));display:flex;padding-left:166px}
.nav a{color:#fff;text-decoration:none;font-size:12.5px;line-height:37px;text-align:center;border-right:1px solid #2a2a2a;letter-spacing:0}
.nav a.active{background:linear-gradient(#e2262b,var(--red-dark))}
.panel{left:141px;top:214px;width:921px;height:315px;background:#fff;border-radius:3px;box-shadow:0 0 6px rgba(0,0,0,.18)}
.hero{left:159px;top:232px;width:884px;height:264px;border-radius:4px;background:linear-gradient(90deg,#7c8a70,#b9a79a 35%,#d8dee3 65%,#9fb4c8)}
.heading{top:508px;height:28px;border-bottom:1px solid var(--rule)}
.heading span{display:inline-block;height:28px;padding:0 18px;border-radius:4px 14px 0 0;color:#fff;font-size:18px;font-weight:700;line-height:28px;letter-spacing:0}
.h-left{left:158px;width:528px}
.h-left span{background:linear-gradient(#ff8a2a,var(--orange));width:152px}
.h-right{left:714px;width:348px}
.h-right span{background:linear-gradient(#777,#333);width:192px}
.col-left{left:158px;top:548px;width:505px}
.col-left p{margin-bottom:13.6px}
.sites{left:158px;top:727px;width:494px;height:115px;border-radius:4px;background:linear-gradient(#c4c4c4,#f2f2f2)}
.sites-head{position:absolute;left:10px;top:9px;width:474px;height:28px;border-radius:3px;background:linear-gradient(#fff,#e4e4e4);font-weight:700;color:#111;font-size:12px;line-height:28px;padding-left:9px;letter-spacing:0}
.sites ul{position:absolute;top:50px;list-style:none}
.sites li{height:28px;color:var(--link)}
.sites li::before{content:"\25B8";color:#555;margin-right:6px;font-size:9px}
.sites .a{left:18px}.sites .b{left:248px}
.sites .sep{position:absolute;left:208px;top:50px;width:1px;height:60px;background:#aaa}
.photo{left:714px;top:557px;width:188px;height:160px;border-radius:3px;background:linear-gradient(#6d5a4a,#b8a58f 55%,#cfc6bb)}
.side-text{left:920px;top:556px;width:144px}
.col-right{left:714px;top:733px;width:350px}
.footer{left:159px;top:883px;width:884px;height:82px}
.footer-links{left:177px;top:907px;display:flex;gap:14px;color:#111;font-size:12.5px;letter-spacing:0}
.footer-links span::before{content:"\2022 "}
.follow{left:814px;top:904px;color:#fff;font-weight:700;font-size:12px;letter-spacing:0}
.social{top:898px;width:30px;height:30px;border-radius:5px;border:2px solid #fff}
.copyright{left:534px;top:950px;color:#666;font-size:12px;letter-spacing:0}
</style>
</head>
<body>
<div class="backdrop"></div>
<div class="abs logo"><span>Pravelo</span></div>
<div class="abs divider"></div>
<div class="abs site-title">Pravelo Onderzoek</div>
<div class="abs tagline">Pravelo is gespecialiseerd in online gegevensverzameling....</div>
<nav class="abs nav">
  <a class="active" style="width:86px">Algemen</a><a style="width:89px">Producten</a><a style="width:75px">Demo's</a><a style="width:67px">Media</a><a style="width:99px">Referenties</a><a style="width:92px">Personeel</a><a style="width:79px">Contact</a>
</nav>
<div class="abs panel"></div>
<div class="abs hero" role="img" aria-label="Foto van onderzoekers aan het werk achter computers"></div>
<div class="abs heading h-left"><span>Pravelo</span></div>
<div class="abs heading h-right"><span>Dataverzameling</span></div>
<div class="abs col-left">
  <p>Pravelo is gespecialiseerd in online gegevensverzameling en analyse en is werkzaam voor internationale opdrachtgevers.</p>
  <p>Het bedrijf werd opgericht in 2004 en is gevestigd in Westerhaven, een kleine havenplaats aan de kust. Onze produkten zijn ontwikkeld op basis van Quanta, een krachtige en uitermate flexibele onderzoekstool voor het verzamelen &amp; verwerken van (online) researchgegevens. Quanta werd ontwikkeld dóór opinieonderzoekers vóór opinieonderzoekers.</p>
  <p>Ons team bestaat uit zowel opinieonderzoekers als programmeurs met vele jaren ervaring op het gebied van opinieonderzoek en met name met online toepassingen daarvoor.</p>
</div>
<div class="abs sites">
  <div class="sites-head">Deze bekende sites zijn ontwikkeld en worden beheerd door Pravelo BV:</div>
  <ul class="a"><li>www.meetpunt-online.nl</li><li>www.panelkamer.nl</li></ul>
  <div class="sep"></div>
  <ul class="b"><li>www.meetpunt-online.nl</li><li>www.panelkamer.nl</li></ul>
</div>
<div class="abs photo" role="img" aria-label="Foto van een bibliotheek met mensen achter computers"></div>
<div class="abs side-text">Pravelo is uitgegroeid tot een volwaardig speler in de markt met een indrukwekkend(e) portfolio. Zo heeft Pravelo sinds haar oprichting wereldwijd meer dan 2.000.000 vragenlijsten afgenomen in diverse talen en voor diverse opdrachtgevers.</div>
<div class="abs col-right">Onze dienstverlening beperkt zich tot het verzamelen van data, Pravelo trekt geen conclusies maar stelt haar klanten middels ons online analyse product Quanta Tables in staat zelf conclusies en/of rapportages te maken zodat beslissingen kunnen worden genomen op basis van eigen waarnemingen.</div>
<svg class="abs footer" width="884" height="82" viewBox="0 0 884 82">
  <defs>
    <linearGradient id="g" x1="0" y1="0" x2="0" y2="1"><stop offset="0" stop-color="#d3ec96"/><stop offset="1" stop-color="#9cc24c"/></linearGradient>
  </defs>
  <path d="M4 0H880a4 4 0 0 1 4 4V55a4 4 0 0 1-4 4H385L345 82H4a4 4 0 0 1-4-4V4a4 4 0 0 1 4-4z" fill="url(#g)"/>
  <path d="M657 0H880a4 4 0 0 1 4 4V55a4 4 0 0 1-4 4H657L619 30z" fill="#8fb43f" opacity=".85"/>
</svg>
<div class="abs footer-links"><span>Algemen</span><span>Producten</span><span>Demo's</span><span>Media</span><span>Referenties</span><span>Personeel</span><span>Contact</span></div>
<div class="abs follow">Follow Us</div>
<div class="abs social" style="left:891px;background:#5bc3ea"></div>
<div class="abs social" style="left:926px;background:#3b5b9a"></div>
<div class="abs social" style="left:962px;background:#1a7bb0"></div>
<div class="abs social" style="left:999px;background:#f07b1a"></div>
<div class="abs copyright">© Pravelo Onderzoek. All Rights Reserved.</div>
</body>
</html>
```